Independent Financial Advisor Billboard Campaign - Granite Bridge Financial

I am a local, independent financial advisor. My company is Granite Bridge Financial, located in Charleston, WV. My main source of revenue comes from those nearing or entering retirement that need assistance with financial planning and investment management. Many are looking to rollover their employer retirement plan into an IRA account. I would like a billboard design campaign that focuses on this type of client. Please see our website www.granitebridgefinancial-example.com for more information.

```html
<!DOCTYPE html>
<html lang="en">
<head>
<meta charset="utf-8">
<title>Granite Bridge Financial – Billboard</title>
<link rel="stylesheet" href="https://fonts.googleapis.com/css2?family=Archivo+Black&family=Archivo:wght@600;700&family=Barlow:wght@500&display=swap">
<style>
  :root{
    --stage:#474747;
    --blue-deep:#05176a;
    --blue-mid:#0d2c9e;
    --blue-ink:#0a1e78;
    --lime:#a8dc00;
    --white:#ffffff;
    --silver-hi:#ffffff;
    --silver-lo:#9da3b0;
    --rule:#c9cfdc;
  }
  *{margin:0;padding:0;box-sizing:border-box}
  html,body{width:1071px;height:1200px;overflow:hidden;background:var(--stage)}
  .billboard{
    position:absolute;left:36px;top:433px;width:1000px;height:333px;overflow:hidden;
    background:radial-gradient(ellipse at 45% 40%, var(--blue-mid) 0%, #0a2488 45%, var(--blue-deep) 100%);
  }
  .billboard__band{position:absolute;inset:0;width:100%;height:100%}
  .headline-rule{position:absolute;left:40px;width:918px;height:2px;background:var(--rule)}
  .headline-rule--top{top:19px}
  .headline-rule--bottom{top:98px}
  .headline{
    position:absolute;left:40px;top:27px;width:918px;text-align:center;white-space:nowrap;z-index:2;
    font-family:"Archivo Black",sans-serif;font-size:55px;line-height:66px;letter-spacing:0;
    background:linear-gradient(180deg,var(--silver-hi) 0%,#e4e7ee 40%,var(--silver-lo) 60%,#f2f4f8 100%);
    -webkit-background-clip:text;background-clip:text;color:transparent;
    filter:drop-shadow(2px 3px 0 #040f4a);
  }
  .brand{
    position:absolute;left:44px;top:140px;display:flex;align-items:center;gap:14px;
  }
  .brand__mark{width:30px;height:30px;background:var(--white);flex:none}
  .brand__name{
    font-family:"Archivo",sans-serif;font-weight:600;font-size:30px;color:var(--white);line-height:1.1;width:300px;
  }
  .advisor-photo{
    position:absolute;left:421px;top:104px;width:208px;height:229px;z-index:1;
    border-radius:90px 90px 0 0;
    background:linear-gradient(180deg,#d9b8a0 0%,#e8e8ec 40%,#f4f4f6 100%);
  }
  .services{
    list-style:none;
    position:absolute;left:636px;top:130px;display:grid;grid-template-columns:185px 170px;row-gap:22px;
  }
  .service{display:flex;align-items:center;gap:14px}
  .service__icon{width:40px;height:40px;flex:none}
  .service__label{
    font-family:"Archivo",sans-serif;font-weight:700;font-size:19px;line-height:21px;color:var(--white);text-transform:uppercase;white-space:nowrap;
  }
  .phone{
    position:absolute;left:84px;top:278px;white-space:nowrap;
    font-family:"Archivo Black",sans-serif;font-size:40px;line-height:46px;color:var(--blue-ink);
  }
  .website{
    position:absolute;left:632px;top:288px;width:338px;text-align:right;white-space:nowrap;
    font-family:"Barlow",sans-serif;font-weight:500;font-size:16px;line-height:22px;color:var(--blue-ink);
  }
</style>
</head>
<body>
<main class="billboard">
  <svg class="billboard__band" viewBox="0 0 1000 333" preserveAspectRatio="none" aria-hidden="true">
    <defs>
      <linearGradient id="swoosh" x1="0" x2="1">
        <stop offset="0" stop-color="#8e95a3"/>
        <stop offset="0.5" stop-color="#ffffff"/>
        <stop offset="1" stop-color="#8e95a3"/>
      </linearGradient>
    </defs>
    <path d="M0,238 Q500,300 1000,238 L1000,333 L0,333 Z" fill="var(--lime)"/>
    <path d="M18,228 Q500,292 982,228 Q500,282 18,228 Z" fill="url(#swoosh)"/>
  </svg>

  <div class="headline-rule headline-rule--top"></div>
  <h1 class="headline">RETIREMENT DONE RIGHT</h1>
  <div class="headline-rule headline-rule--bottom"></div>

  <div class="brand">
    <span class="brand__mark"></span>
    <span class="brand__name">Granite Bridge Financial</span>
  </div>

  <div class="advisor-photo" role="img" aria-label="Portrait photo of the advisor in a white polo shirt"></div>

  <ul class="services">
    <li class="service">
      <svg class="service__icon" viewBox="0 0 40 40" fill="none" stroke="var(--lime)" stroke-width="1.6" aria-hidden="true">
        <path d="M14 12 Q22 2 30 12 Z"/><path d="M22 10 L18 30"/><path d="M4 30 L26 30 L32 22"/><path d="M8 30 L6 36 M24 30 L26 36"/>
      </svg>
      <span class="service__label">Retirement<br>Planning</span>
    </li>
    <li class="service">
      <svg class="service__icon" viewBox="0 0 40 40" fill="none" stroke="var(--lime)" stroke-width="1.6" aria-hidden="true">
        <path d="M10 6 H30 Q26 12 28 20 Q30 28 26 34 H6 Q10 28 8 20 Q6 12 10 6 Z"/><circle cx="28" cy="31" r="3"/>
      </svg>
      <span class="service__label">Estate<br>Planning</span>
    </li>
    <li class="service">
      <svg class="service__icon" viewBox="0 0 40 40" fill="none" stroke="var(--lime)" stroke-width="1.6" aria-hidden="true">
        <path d="M4 14 L20 4 L36 14 Z"/><path d="M6 14 H34 V17 H6 Z"/><path d="M10 17 V31 M16 17 V31 M24 17 V31 M30 17 V31"/><path d="M5 31 H35 V35 H5 Z"/>
      </svg>
      <span class="service__label">College<br>Planning</span>
    </li>
    <li class="service">
      <svg class="service__icon" viewBox="0 0 40 40" fill="none" stroke="var(--lime)" stroke-width="1.6" aria-hidden="true">
        <path d="M3 9 H15 L18 12 H37 V34 H3 Z"/><circle cx="20" cy="23" r="6"/><path d="M20 19 V26 M17 23 L20 26 L23 23"/>
      </svg>
      <span class="service__label">Helpful<br>Advice</span>
    </li>
  </ul>

  <p class="phone">304.555.0187</p>
  <p class="website">www.granitebridgefinancial-example.com</p>
</main>
</body>
</html>
```